I need some graphic design. A one page graphic to be emailed to a mailing list and posted on all social media platforms. Header of flyer - “Announcing the launch of Meridale Lodges Retreats and Sloops” . One evocative image (I welcome suggestions or I will provide) and copy with contact details for click through (again, welcome suggestions or I can provide) www.meridalelrs.example

```html
<!DOCTYPE html>
<html lang="en">
<head>
<meta charset="utf-8">
<title>Meridale Lodges Retreats and Sloops – Launch</title>
<link href="https://fonts.googleapis.com/css2?family=Nunito:wght@300;700;800&display=swap" rel="stylesheet">
<style>
  :root {
    --header-band: #8b98d0;
    --brand-ink: #3a52a8;
    --white: #ffffff;
    --sky-deep: #2358b3;
    --sky-mid: #3f72c4;
    --sky-soft: #7f93cf;
    --dusk-peach: #d9a99c;
    --shore-teal: #4f9a98;
    --button-top: #3a7fe0;
    --button-bottom: #1d4fb0;
    --button-ring: #cfe0ff;
  }
  html, body {
    margin: 0;
    padding: 0;
    width: 873px;
    height: 1200px;
    overflow: hidden;
    background: #ffffff;
  }
  .flyer {
    position: relative;
    width: 873px;
    height: 1200px;
    overflow: hidden;
    font-family: "Nunito", sans-serif;
    color: var(--white);
  }
  .header-band {
    position: absolute;
    left: 0; top: 0;
    width: 100%;
    height: 248px;
    background: var(--header-band);
    display: flex;
    flex-direction: column;
    align-items: center;
    justify-content: center;
    gap: 10px;
  }
  .brand-row {
    display: flex;
    align-items: center;
    gap: 18px;
  }
  .brand-dot {
    width: 58px;
    height: 58px;
    border-radius: 50%;
    background: var(--brand-ink);
  }
  .brand-name {
    font-weight: 300;
    font-size: 50px;
    letter-spacing: 3px;
    color: var(--brand-ink);
    text-transform: uppercase;
  }
  .brand-web {
    font-weight: 300;
    font-size: 17px;
    letter-spacing: 3px;
    color: var(--brand-ink);
  }
  .scene {
    position: absolute;
    left: 0; top: 248px;
    width: 100%;
    height: 952px;
    background: linear-gradient(180deg,
      var(--sky-deep) 0%,
      var(--sky-mid) 30%,
      var(--sky-soft) 48%,
      var(--dusk-peach) 64%,
      #8a8a7a 78%,
      var(--shore-teal) 100%);
  }
  .headline {
    position: absolute;
    left: 0; top: 285px;
    width: 100%;
    text-align: center;
    margin: 0;
    font-weight: 700;
  }
  .headline .lead {
    display: block;
    font-size: 30px;
    line-height: 40px;
  }
  .headline .name-main {
    display: block;
    font-size: 72px;
    line-height: 96px;
    font-weight: 800;
    margin-top: 6px;
  }
  .headline .name-line {
    display: block;
    font-size: 52px;
    line-height: 70px;
  }
  .headline .name-tail {
    display: block;
    font-size: 46px;
    line-height: 70px;
  }
  .quote {
    position: absolute;
    left: 0; top: 655px;
    width: 100%;
    margin: 0;
    font-weight: 700;
    font-size: 22px;
    line-height: 34px;
    text-align: center;
  }
  .quote-row {
    display: flex;
    align-items: center;
    justify-content: center;
    gap: 8px;
  }
  .dash-rule {
    width: 168px;
    height: 2px;
    background: repeating-linear-gradient(90deg, var(--white) 0 9px, transparent 9px 16px);
  }
  .quote-author {
    display: block;
    text-align: right;
    padding-right: 220px;
  }
  .learn-more {
    position: absolute;
    left: 597px; top: 1072px;
    width: 213px;
    height: 68px;
    border-radius: 34px;
    background: linear-gradient(180deg, var(--button-top), var(--button-bottom));
    box-shadow: 0 3px 8px rgba(0,0,0,0.35);
    display: flex;
    align-items: center;
    justify-content: space-between;
    padding: 0 8px 0 22px;
    box-sizing: border-box;
    font-weight: 700;
    font-size: 23px;
    color: var(--white);
    text-decoration: none;
  }
  .learn-more svg { display: block; }
</style>
</head>
<body>
  <main class="flyer">
    <header class="header-band">
      <div class="brand-row">
        <span class="brand-dot"></span>
        <span class="brand-name">Meridale</span>
      </div>
      <span class="brand-web">www.meridalelrs.example</span>
    </header>

    <div class="scene" role="img" aria-label="Photograph of a tropical beach resort at dusk: thatched huts lit along the sand, palm trees, and a lantern-lined wooden boardwalk over calm turquoise water under a blue-to-peach sky"></div>

    <h1 class="headline">
      <span class="lead">Announcing the launch of</span>
      <span class="name-main">Meridale</span>
      <span class="name-line">Lodges Retreats</span>
      <span class="name-tail">and Sloops</span>
    </h1>

    <blockquote class="quote">
      <span class="quote-row"><span class="dash-rule"></span>“Traveling – it leaves you speechless,<span class="dash-rule"></span></span>
      <span>then turns you into a storyteller.”</span>
      <span class="quote-author">– Ilyas Marrow</span>
    </blockquote>

    <a class="learn-more" href="https://www.meridalelrs.example">
      <span>Learn more</span>
      <svg width="54" height="54" viewBox="0 0 54 54" aria-hidden="true">
        <circle cx="27" cy="27" r="25" fill="var(--button-ring)"/>
        <path d="M21 16 L38 27 L21 38 Z" fill="var(--button-bottom)"/>
      </svg>
    </a>
  </main>
</body>
</html>
```